Wood Logging Stationary design

We need a new company logo for our stationary. Be creative. Most company apparel and hats are Navy blue and Light gray. Logo does not necessarily have to contain those two colors. Pictures of trees, logging equipment, log trucks, and logs are acceptable but not required. I am open to any and all designs. Logo must reflect our pride and professionalism in the East Texas Timber Industry.
Updates

Target Market(s)

Timber owners and sawmills. Adults 25 years and up

Industry/Entity Type

Industry

Font styles to use
Serif
Decorative

Requirements
Must have
• R. J. Pell Hauling Co.
Nice to have
• Phone number: 936-402-5817
address:
PO Box 4830
Dunmore Flats, TX 77912
www.rjpellhauling.example
rjpellhauling@mailbox.example

```html
<!DOCTYPE html>
<html lang="en">
<head>
<meta charset="utf-8">
<title>R. J. Pell Hauling Co. — Stationery Set</title>
<link rel="stylesheet" href="https://fonts.googleapis.com/css2?family=Exo+2:wght@700;800&family=Roboto+Condensed:wght@400;700&display=swap">
<style>
  :root {
    --brand-blue: #1a2ff0;
    --paper: #ffffff;
    --edge: #b9bcbf;
    --bg-top: #f3f5f5;
    --bg-bottom: #bccac7;
    --muted: #8a8f96;
    --ink-light: #ffffff;
  }
  * { box-sizing: border-box; margin: 0; padding: 0; }
  html, body { width: 1200px; height: 1200px; overflow: hidden; }
  body {
    position: relative;
    background: linear-gradient(to bottom, var(--bg-top) 0%, #e4e9e9 45%, var(--bg-bottom) 100%);
    font-family: "Roboto Condensed", "Arial Narrow", sans-serif;
  }
  .sprite { position: absolute; width: 0; height: 0; }

  /* Company name mark */
  .name-mark {
    position: absolute;
    display: flex; align-items: center; justify-content: center; gap: 10px;
    font-family: "Exo 2", sans-serif; font-weight: 800;
    color: var(--brand-blue); text-align: center; line-height: 1.05;
  }
  .name-mark .dot { border-radius: 50%; background: currentColor; flex: none; }
  .name-mark.on-blue { color: var(--ink-light); }

  .hero-mark { left: 150px; top: 215px; width: 310px; height: 100px; font-size: 34px; }
  .hero-mark .dot { width: 22px; height: 22px; }

  /* Business cards */
  .card {
    position: absolute; top: 152px; width: 251px; height: 388px;
    border-radius: 11px; overflow: hidden;
    box-shadow: 0 2px 4px rgba(0,0,0,.25);
  }
  .card--blue { left: 595px; background: var(--brand-blue); }
  .card--white { left: 871px; background: var(--paper); border: 1px solid #d4d7d9; }
  .card .name-mark { left: 20px; top: 70px; width: 211px; height: 90px; font-size: 21px; }
  .card .name-mark .dot { width: 14px; height: 14px; }
  .card__person {
    position: absolute; left: 0; right: 0; top: 200px; text-align: center;
  }
  .card__name {
    font-family: "Exo 2", sans-serif; font-weight: 800; font-size: 21px; letter-spacing: .5px;
  }
  .card__role { font-size: 9.5px; margin-top: 2px; }
  .card--blue .card__name, .card--blue .card__role { color: var(--ink-light); }
  .card--white .card__name { color: var(--brand-blue); }
  .card--white .card__role { color: var(--muted); }
  .card__rule { position: absolute; left: 0; right: 0; top: 278px; height: 1px; background: rgba(255,255,255,.35); }
  .card__band { position: absolute; left: 0; right: 0; top: 279px; bottom: 0; background: var(--brand-blue); }
  .card__contacts {
    position: absolute; left: 50px; top: 296px; list-style: none;
    color: var(--ink-light); font-size: 9.5px;
  }
  .card__contacts li { height: 14.5px; display: flex; align-items: center; }
  .card__contacts .ico { width: 9px; height: 9px; margin-right: 13px; fill: var(--ink-light); flex: none; }
  .card__contacts li.cont .ico { visibility: hidden; }

  /* Letterhead */
  .letterhead {
    position: absolute; left: 76px; top: 410px; width: 453px; height: 641px;
    background: var(--paper); border: 1px solid var(--edge);
    box-shadow: 0 2px 4px rgba(0,0,0,.15);
  }
  .letterhead .name-mark { left: 18px; top: 28px; width: 110px; height: 66px; font-size: 13px; gap: 6px; justify-content: flex-start; }
  .letterhead .name-mark .dot { width: 9px; height: 9px; }

  .footer-band {
    position: absolute; left: 0; right: 0; bottom: 0;
    background: var(--brand-blue); color: var(--ink-light);
    display: flex; align-items: center; justify-content: center; gap: 8px;
    font-weight: 700; white-space: nowrap;
  }
  .footer-band span { display: flex; align-items: center; }
  .footer-band .ico { fill: var(--ink-light); margin-right: 3px; }
  .letterhead .footer-band { height: 42px; font-size: 8px; gap: 6px; }
  .letterhead .footer-band .ico { width: 8px; height: 8px; }

  /* Envelope */
  .envelope__flap { position: absolute; left: 583px; top: 683px; width: 531px; height: 108px; }
  .envelope {
    position: absolute; left: 583px; top: 790px; width: 531px; height: 261px;
    background: var(--paper); border: 1px solid var(--edge);
    box-shadow: 0 2px 4px rgba(0,0,0,.15);
  }
  .envelope .name-mark { left: 24px; top: 20px; width: 110px; height: 70px; font-size: 13px; gap: 6px; justify-content: flex-start; }
  .envelope .name-mark .dot { width: 9px; height: 9px; }
  .envelope .footer-band { height: 30px; font-size: 10px; }
  .envelope .footer-band .ico { width: 9px; height: 9px; }
</style>
</head>
<body>

<svg class="sprite" aria-hidden="true">
  <symbol id="i-phone" viewBox="0 0 16 16"><path d="M2 5c0-2 2-3 6-3s6 1 6 3v1h-3V4.5H5V6H2zM4 7h8l2 6H2z"/></symbol>
  <symbol id="i-home" viewBox="0 0 16 16"><path d="M8 1l7 7h-2v7H9.5v-4h-3v4H3V8H1z"/></symbol>
  <symbol id="i-globe" viewBox="0 0 16 16"><path d="M8 1a7 7 0 100 14A7 7 0 008 1zm0 1.3c.8.7 1.5 2 1.8 3.7H6.2C6.5 4.3 7.2 3 8 2.3zM2.5 7h3.4v2H2.5zm4.4 0h2.2v2H6.9zm3.2 0h3.4v2h-3.4zM6.2 10h3.6c-.3 1.7-1 3-1.8 3.7-.8-.7-1.5-2-1.8-3.7zM3 6a5.8 5.8 0 012.5-3 8 8 0 00-.6 3zm8.1 0a8 8 0 00-.6-3A5.8 5.8 0 0113 6zM3 10h1.9a8 8 0 00.6 3A5.8 5.8 0 013 10zm8.1 0H13a5.8 5.8 0 01-2.5 3 8 8 0 00.6-3z"/></symbol>
  <symbol id="i-mail" viewBox="0 0 16 16"><path d="M1 3h14v10H1zm1.5 1.5v.3L8 9l5.5-4.2v-.3zM2.5 6.6v5h11v-5L8 10.8z"/></symbol>
</svg>

<!-- Primary mark -->
<div class="name-mark hero-mark"><span class="dot"></span><span>R. J. Pell<br>Hauling Co.</span></div>

<!-- Business card: blue -->
<section class="card card--blue">
  <div class="name-mark on-blue"><span class="dot"></span><span>R. J. Pell<br>Hauling Co.</span></div>
  <div class="card__person">
    <div class="card__name">JOHN DOE</div>
    <div class="card__role">Production Manager</div>
  </div>
  <div class="card__rule"></div>
  <ul class="card__contacts">
    <li><svg class="ico"><use href="#i-phone"/></svg>936-402-5817</li>
    <li><svg class="ico"><use href="#i-home"/></svg>PO Box 4830</li>
    <li class="cont"><svg class="ico"><use href="#i-home"/></svg>Dunmore Flats, TX 77912</li>
    <li><svg class="ico"><use href="#i-globe"/></svg>www.rjpellhauling.example</li>
    <li><svg class="ico"><use href="#i-mail"/></svg>rjpellhauling@mailbox.example</li>
  </ul>
</section>

<!-- Business card: white -->
<section class="card card--white">
  <div class="name-mark"><span class="dot"></span><span>R. J. Pell<br>Hauling Co.</span></div>
  <div class="card__person">
    <div class="card__name">JOHN DOE</div>
    <div class="card__role">Production Manager</div>
  </div>
  <div class="card__band"></div>
  <ul class="card__contacts">
    <li><svg class="ico"><use href="#i-phone"/></svg>936-402-5817</li>
    <li><svg class="ico"><use href="#i-home"/></svg>PO Box 4830</li>
    <li class="cont"><svg class="ico"><use href="#i-home"/></svg>Dunmore Flats, TX 77912</li>
    <li><svg class="ico"><use href="#i-globe"/></svg>www.rjpellhauling.example</li>
    <li><svg class="ico"><use href="#i-mail"/></svg>rjpellhauling@mailbox.example</li>
  </ul>
</section>

<!-- Letterhead -->
<section class="letterhead">
  <div class="name-mark"><span class="dot"></span><span>R. J. Pell<br>Hauling Co.</span></div>
  <footer class="footer-band">
    <span><svg class="ico"><use href="#i-phone"/></svg>936-402-5817</span>
    <span><svg class="ico"><use href="#i-home"/></svg>PO Box 4830 Dunmore Flats, TX 77912</span>
    <span><svg class="ico"><use href="#i-globe"/></svg>www.rjpellhauling.example</span>
    <span><svg class="ico"><use href="#i-mail"/></svg>rjpellhauling@mailbox.example</span>
  </footer>
</section>

<!-- Envelope -->
<svg class="envelope__flap" viewBox="0 0 531 108" aria-hidden="true">
  <path d="M0 108 V80 C0 62 12 56 40 48 C140 20 220 2 265 2 C310 2 390 20 491 48 C519 56 531 62 531 80 V108 Z" fill="var(--brand-blue)"/>
</svg>
<section class="envelope">
  <div class="name-mark"><span class="dot"></span><span>R. J. Pell<br>Hauling Co.</span></div>
  <footer class="footer-band">
    <span><svg class="ico"><use href="#i-phone"/></svg>936-402-5817</span>
    <span><svg class="ico"><use href="#i-home"/></svg>PO Box 4830 Dunmore Flats, TX 77912</span>
    <span><svg class="ico"><use href="#i-globe"/></svg>www.rjpellhauling.example</span>
    <span><svg class="ico"><use href="#i-mail"/></svg>rjpellhauling@mailbox.example</span>
  </footer>
</section>

</body>
</html>
```